Visitenkarten-Design für private und gesellschaftliche Anlässe gesucht
Zielgruppe
Es handelt sich um eine Visitenkarte für den privaten Bereich, bzw. für private und Gesellschaftliche Anlässe
Aufgabenstellung
Zunächst die Kontaktdaten
Roland Kettwig
Postfach 3087
mail@rolandkettwig.de
Des weiteren soll der Spruch 'Gnothi seauton ' (altgr. Erkenne dich selbst) auf der Karte stehen. Gerne auch auf der Rückseite oder an einer anderen prominenten Stelle
Schön wäre es auch, wenn die I Punkte in meinem Namen farblich etwas hervorgehoben sind und auch so noch einmal an anderer stelle zu finden sind.
Ich habe meine ungefähre Vorstellung als Skizze angehängt, ansonsten gerne auch noch einmal nachfragen.
Ich bin noch etwas unschlüssig, ob die Karte ein klassisches Format erhalten soll oder es doch Quadratisch wird.

```html
<!DOCTYPE html>
<html lang="de">
<head>
<meta charset="utf-8">
<title>Visitenkarte Roland Kettwig</title>
<link rel="stylesheet" href="https://fonts.googleapis.com/css2?family=Cormorant+Garamond:wght@500&family=Barlow+Condensed:wght@400&display=swap">
<style>
  :root {
    --page: #ffffff;
    --card: #ffffff;
    --accent: #3673b0;
    --ink: #111111;
    --dot-light: #ffffff;
    --shadow: rgba(0, 0, 0, 0.35);
  }
  html, body {
    margin: 0;
    padding: 0;
    overflow: hidden;
    background: var(--page);
  }
  .canvas {
    position: relative;
    width: 1200px;
    height: 675px;
    background: var(--page);
    overflow: hidden;
  }
  .card {
    position: absolute;
    background: var(--card);
    box-shadow: 0 1px 4px var(--shadow);
    overflow: hidden;
  }
  .card--front {
    left: 148px;
    top: 234px;
    width: 345px;
    height: 224px;
  }
  .card--back {
    left: 647px;
    top: 222px;
    width: 368px;
    height: 237px;
  }
  .card__band {
    position: absolute;
    left: 0;
    right: 0;
    bottom: 0;
    background: var(--accent);
  }
  .card--front .card__band { height: 41px; }
  .card--back .card__band { height: 43px; }
  .dot {
    position: absolute;
    width: 4px;
    height: 4px;
    background: var(--accent);
  }
  .dot--light { background: var(--dot-light); }
  .motto {
    position: absolute;
    left: 0;
    right: 0;
    top: 72px;
    margin: 0;
    text-align: center;
    font-family: "Cormorant Garamond", "Times New Roman", serif;
    font-weight: 500;
    font-size: 34px;
    letter-spacing: 0.2px;
    color: var(--ink);
  }
  .contact {
    position: absolute;
    left: 167px;
    top: 64px;
    margin: 0;
    font-family: "Barlow Condensed", "Arial Narrow", sans-serif;
    font-weight: 400;
    font-size: 19px;
    line-height: 26px;
    letter-spacing: -0.2px;
    color: var(--ink);
    font-style: normal;
  }
  .contact__line { display: block; }
</style>
</head>
<body>
<main class="canvas">
  <section class="card card--front" aria-label="Vorderseite">
    <span class="dot" style="left:241px; top:20px;"></span>
    <span class="dot" style="left:274px; top:20px;"></span>
    <span class="dot" style="left:307px; top:20px;"></span>
    <p class="motto">Gnothi seauton</p>
    <div class="card__band"></div>
    <span class="dot dot--light" style="left:27px; top:201px;"></span>
    <span class="dot dot--light" style="left:59px; top:201px;"></span>
    <span class="dot dot--light" style="left:92px; top:201px;"></span>
  </section>

  <section class="card card--back" aria-label="Rückseite">
    <span class="dot" style="left:263px; top:23px;"></span>
    <span class="dot" style="left:298px; top:23px;"></span>
    <span class="dot" style="left:333px; top:23px;"></span>
    <address class="contact">
      <span class="contact__line">Roland Kettwig</span>
      <span class="contact__line">Postfach 3087</span>
      <span class="contact__line">+49 1523 4817306</span>
      <span class="contact__line">mail@rolandkettwig.de</span>
    </address>
    <div class="card__band"></div>
    <span class="dot dot--light" style="left:28px; top:213px;"></span>
    <span class="dot dot--light" style="left:63px; top:213px;"></span>
    <span class="dot dot--light" style="left:98px; top:213px;"></span>
  </section>
</main>
</body>
</html>
```